KRT Cartridge chip board folding ammuniton boxes for retail sale

Design a scalable design for use with 20 round and 50 round boxes for Ammunition. The caliber will be 9mm but will need to be editable, all warnings and barcodes will need to be able to be edited also. I have attached the company logo.

**UPDATE**
Box dimensions
20rd= 2.55in long X 2.1in width X 1.25in height

50rd= 5.1in long x 2.6in width X 1.2in height

Please see the bullet picture i would like used if possible.

Target Market(s)

Quality shooting sports, self defense

Industry/Entity Type

Self Defense

Requirements
Must have
• supplied company logo design
Should not have
• any cartoons of any kind

```html
<!DOCTYPE html>
<html lang="en">
<head>
<meta charset="utf-8">
<title>KRT Cartridge – 9mm Box Dielines</title>
<link href="https://fonts.googleapis.com/css2?family=Arvo:wght@700&family=Montserrat:wght@700;900&family=Oswald:wght@500;600&family=Roboto+Condensed:wght@400;700&display=swap" rel="stylesheet">
<style>
  :root {
    --bg-top: #3ff5d0;
    --bg-bottom: #c4fbf2;
    --ink: #0d0d0d;
    --red: #e21f26;
    --white: #ffffff;
    --steel-light: #d4d4d4;
    --steel-dark: #9a9a9a;
    --note: #a3161b;
  }
  * { margin: 0; padding: 0; box-sizing: border-box; }
  html, body { width: 1108px; height: 1200px; overflow: hidden; }
  body {
    background: linear-gradient(180deg, var(--bg-top), var(--bg-bottom));
    position: relative;
    font-family: "Montserrat", sans-serif;
  }
  .designer-note {
    position: absolute;
    top: 225px; left: 0; width: 1108px;
    text-align: center;
    font-family: "Arvo", serif;
    font-weight: 700;
    font-size: 21px;
    line-height: 26px;
    color: var(--note);
  }
  .dielines {
    position: absolute;
    top: 340px; left: 0;
    width: 1108px; height: 621px;
  }
  .brand { font-family: "Montserrat", sans-serif; font-weight: 900; fill: var(--ink); }
  .count { font-family: "Montserrat", sans-serif; font-weight: 900; }
  .count-label { font-family: "Montserrat", sans-serif; font-weight: 700; }
  .caliber { font-family: "Oswald", sans-serif; font-weight: 600; fill: var(--red); }
  .spec { font-family: "Roboto Condensed", sans-serif; font-weight: 700; fill: var(--ink); }
  .fine { font-family: "Roboto Condensed", sans-serif; font-weight: 400; fill: var(--white); }
  .fine-bold { font-weight: 700; }
  .origin { font-family: "Montserrat", sans-serif; font-weight: 700; fill: var(--white); }
</style>
</head>
<body>

<p class="designer-note">because i am not sure<br>the right bullet for 50rd (115gr FMJ)<br>i created 2 different bullet picture in this design</p>

<svg class="dielines" viewBox="0 940 1848 1035" xmlns="http://www.w3.org/2000/svg">
  <defs>
    <linearGradient id="steel" x1="0" y1="0" x2="1" y2="1">
      <stop offset="0" stop-color="var(--steel-light)"/>
      <stop offset="0.5" stop-color="#b8b8b8"/>
      <stop offset="1" stop-color="var(--steel-dark)"/>
    </linearGradient>
    <linearGradient id="round-nose" x1="0" y1="0" x2="1" y2="0">
      <stop offset="0" stop-color="#8a5a32"/>
      <stop offset="0.5" stop-color="#e3a27a"/>
      <stop offset="1" stop-color="#a3763d"/>
    </linearGradient>
    <linearGradient id="hollow-point" x1="0" y1="0" x2="1" y2="0">
      <stop offset="0" stop-color="#7b6a2c"/>
      <stop offset="0.5" stop-color="#e0c27a"/>
      <stop offset="1" stop-color="#8c7434"/>
    </linearGradient>

    <!-- 50 round front face -->
    <g id="face50-core">
      <rect x="290" y="1395" width="470" height="220" fill="var(--ink)"/>
      <polygon points="290,1398 700,1398 760,1460 760,1615 752,1615 625,1480 290,1480" fill="var(--white)"/>
      <polygon points="290,1476 627,1476 756,1615 290,1615" fill="var(--red)"/>
      <polygon points="290,1482 622,1482 748,1615 290,1615" fill="url(#steel)"/>
      <rect x="405" y="1482" width="0" height="0"/>
      <text class="brand" x="318" y="1448" font-size="40">KRT Cartridge</text>
      <circle cx="640" cy="1436" r="20" fill="none" stroke="var(--red)" stroke-width="5"/>
      <text class="count" x="704" y="1443" font-size="44" fill="var(--red)" text-anchor="middle">50</text>
      <text class="count-label" x="704" y="1464" font-size="16" fill="var(--red)" text-anchor="middle">rounds</text>
      <text class="caliber" x="417" y="1543" font-size="22">9MM 115GR FMJ</text>
      <text class="spec" x="417" y="1563" font-size="12">Full Metal Jacket</text>
      <text class="spec" x="417" y="1579" font-size="12">Centerfire Pistol Cartdges</text>
      <text class="spec" x="417" y="1595" font-size="12">Non-Corrosive</text>
    </g>

    <!-- 20 round front face, local coords 235 x 175 -->
    <g id="face20">
      <rect x="0" y="0" width="235" height="175" fill="url(#steel)"/>
      <polygon points="0,0 235,0 235,50 60,50 0,0" fill="var(--white)"/>
      <polygon points="0,0 62,50 235,50 235,54 58,54 0,6" fill="var(--red)"/>
      <text class="brand" x="70" y="34" font-size="18">KRT Cartridge</text>
      <circle cx="48" cy="27" r="10" fill="none" stroke="var(--red)" stroke-width="3"/>
      <rect x="0" y="54" width="44" height="121" fill="var(--ink)"/>
      <rect x="14" y="70" width="16" height="58" rx="6" fill="url(#hollow-point)" role="img" aria-label="9mm jacketed hollow point cartridge photo"/>
      <text class="caliber" x="52" y="100" font-size="15" transform="rotate(0)">9MM 124GR JHP</text>
      <text class="spec" x="52" y="116" font-size="9">Jacketed Hollow Point</text>
      <text class="spec" x="52" y="128" font-size="9">Centerfire Pistol Cartdges</text>
      <text class="spec" x="52" y="140" font-size="9">Non-Corrosive</text>
      <polygon points="175,150 235,130 235,175 165,175" fill="var(--red)"/>
      <text class="count" x="208" y="168" font-size="18" fill="var(--white)" text-anchor="middle">20</text>
    </g>

    <!-- full 50 round dieline -->
    <g id="dieline50">
      <!-- side flaps -->
      <rect x="130" y="1725" width="170" height="240" rx="10" fill="var(--ink)"/>
      <rect x="750" y="1725" width="170" height="240" rx="10" fill="var(--ink)"/>
      <text class="origin" font-size="9" transform="translate(278,1920) rotate(-90)">MADE WITH PRIDE IN THE U.S.A</text>
      <text class="caliber" font-size="40" transform="translate(804,1820) rotate(90)">9MM</text>
      <text class="caliber" font-size="22" style="fill:var(--white)" transform="translate(776,1825) rotate(90)">115GR FMJ</text>

      <!-- top closure panel (upside down) -->
      <g transform="rotate(180 525 1305)">
        <rect x="290" y="1235" width="470" height="140" fill="var(--ink)"/>
        <polygon points="650,1235 760,1235 760,1375 600,1375" fill="var(--red)"/>
        <text class="count" x="695" y="1318" font-size="44" fill="var(--white)" text-anchor="middle">50</text>
        <text class="count-label" x="695" y="1345" font-size="18" fill="var(--white)" text-anchor="middle">rounds</text>
        <text class="brand" x="340" y="1318" font-size="30" style="fill:var(--white)">KRT Cartridge</text>
        <circle cx="560" cy="1308" r="15" fill="none" stroke="var(--red)" stroke-width="4"/>
        <text class="fine" x="310" y="1355" font-size="9" style="fill:var(--red)">WARNING: Keep out of reach of children. Read all warning on package</text>
      </g>

      <!-- front face -->
      <use href="#face50-core"/>

      <!-- warning panel -->
      <rect x="290" y="1615" width="470" height="110" fill="var(--ink)"/>
      <polygon points="650,1615 760,1615 760,1725 600,1725" fill="var(--red)"/>
      <text class="count" x="700" y="1682" font-size="44" fill="var(--white)" text-anchor="middle">50</text>
      <text class="count-label" x="700" y="1705" font-size="18" fill="var(--white)" text-anchor="middle">rounds</text>
      <g class="fine" font-size="8">
        <text x="310" y="1636"><tspan class="fine-bold">WARNING:</tspan> THIS AMMUNITION SHOULD BE USED ONLY IN WELL MAINTAINED</text>
        <text x="310" y="1647">FIREARMS IN GOOD CONDITION AND DESIGNED FOR MODERN AMMUNITION.</text>
        <text x="310" y="1658" class="fine-bold">TO AVOID INJURY:</text>
        <text x="310" y="1669">1. MAKE SURE THAT THIS THE CORRECT CARTRIDGE FOR YOUR FIREARM</text>
        <text x="310" y="1680">2. ALWAYS WEAR EYE PROTECTION.</text>
        <text x="310" y="1691">3. KEEP THE BARREL FREE OF OBSTRUCTIONS</text>
        <text x="310" y="1702">4. IF A MISSFIRE OCCURS, KEEP THE MUZZLE POINTED IN A SAFE DIRECTION</text>
        <text x="318" y="1713">AND USE CARE IN UNLOADING.</text>
      </g>

      <!-- bottom face -->
      <use href="#face50-core" transform="translate(0 330)"/>
    </g>
  </defs>

  <!-- 20 round dieline -->
  <g class="dieline-20">
    <rect x="660" y="955" width="565" height="190" rx="12" fill="var(--ink)"/>
    <text class="caliber" font-size="36" transform="translate(768,1075) rotate(-90)">9MM</text>
    <text class="caliber" font-size="20" style="fill:var(--white)" transform="translate(798,1070) rotate(-90)">124GR JHP</text>
    <rect x="725" y="1085" width="55" height="18" rx="7" fill="url(#hollow-point)" role="img" aria-label="9mm jacketed hollow point cartridge photo"/>
    <text class="origin" font-size="7" transform="translate(1082,995) rotate(90)">MADE WITH PRIDE IN THE U.S.A</text>
    <use href="#face20" transform="translate(1058 1140) rotate(180)"/>

    <rect x="823" y="1145" width="235" height="120" fill="var(--ink)"/>
    <g transform="rotate(180 940 1205)">
      <g class="fine" font-size="6">
        <text x="835" y="1165" class="fine-bold">WARNING: THIS AMMUNITION SHOULD BE USED ONLY IN</text>
        <text x="835" y="1174">WELL MAINTAINED FIREARMS IN GOOD CONDITION AND</text>
        <text x="835" y="1183">DESIGNED FOR MODERN AMMUNITION.</text>
        <text x="835" y="1192" class="fine-bold">TO AVOID INJURY:</text>
        <text x="835" y="1201">1. MAKE SURE THAT THIS THE CORRECT CARTRIDGE FOR</text>
        <text x="835" y="1210">2. ALWAYS WEAR EYE PROTECTION.</text>
        <text x="835" y="1219">3. KEEP THE BARREL FREE OF OBSTRUCTIONS</text>
        <text x="835" y="1228">4. IF A MISSFIRE OCCURS, KEEP THE MUZZLE POINTED IN A</text>
        <text x="835" y="1237">SAFE DIRECTION AND USE CARE IN UNLOADING.</text>
      </g>
      <polygon points="1010,1215 1058,1195 1058,1265 1000,1265" fill="var(--red)"/>
      <text class="count" x="1032" y="1248" font-size="18" fill="var(--white)" text-anchor="middle">20</text>
    </g>

    <use href="#face20" transform="translate(1058 1440) rotate(180)"/>

    <rect x="823" y="1440" width="235" height="157" fill="var(--ink)"/>
    <text class="brand" x="845" y="1498" font-size="16" style="fill:var(--white)">KRT Cartridge</text>
    <circle cx="960" cy="1493" r="8" fill="none" stroke="var(--red)" stroke-width="3"/>
    <polygon points="1000,1470 1048,1458 1048,1540 1000,1525" fill="var(--red)"/>
    <text class="count" x="1026" y="1500" font-size="20" fill="var(--white)" text-anchor="middle">20</text>
    <text class="count-label" x="1026" y="1512" font-size="8" fill="var(--white)" text-anchor="middle">rounds</text>
    <text class="fine" x="843" y="1552" font-size="6" style="fill:var(--red)">WARNING:</text>
    <text class="fine" x="843" y="1561" font-size="6" style="fill:var(--red)">Keep out of reach of children. Read all warning on package</text>
  </g>

  <!-- 50 round dieline, round-nose variant -->
  <g class="dieline-50 variant-round-nose">
    <use href="#dieline50"/>
    <rect x="355" y="1508" width="28" height="82" rx="12" fill="url(#round-nose)" role="img" aria-label="9mm full metal jacket round-nose cartridge photo"/>
    <rect x="355" y="1838" width="28" height="82" rx="12" fill="url(#round-nose)" role="img" aria-label="9mm full metal jacket round-nose cartridge photo"/>
    <rect x="775" y="1788" width="85" height="28" rx="12" fill="url(#round-nose)" role="img" aria-label="9mm full metal jacket round-nose cartridge photo"/>
  </g>

  <!-- 50 round dieline, hollow-point variant -->
  <g class="dieline-50 variant-hollow-point" transform="translate(834 -3)">
    <use href="#dieline50"/>
    <rect x="355" y="1508" width="28" height="82" rx="8" fill="url(#hollow-point)" role="img" aria-label="9mm cartridge photo, alternate bullet"/>
    <rect x="355" y="1838" width="28" height="82" rx="8" fill="url(#hollow-point)" role="img" aria-label="9mm cartridge photo, alternate bullet"/>
    <rect x="775" y="1788" width="85" height="28" rx="8" fill="url(#hollow-point)" role="img" aria-label="9mm cartridge photo, alternate bullet"/>
  </g>
</svg>

</body>
</html>
```